Castastrophe General Contractor needs leave behind for sales

Will respond quickly to designer inquires
Fast winning selection
Will notify all of winning selection

Catastrophe Restoration General Contractor offering specialized services to the insurance industry. Sales meeting leave behind flyer for presentation to insurance agents. We would like for agents to refer policyholders to our company for complete residential and commercial restoration projects.

Some copy uploaded for reference. 5.5" x 8.5" approx - double sided color w/ sales business card reproduced on back side. Approved / Preferred Contractor for Brightshield, Vantacover, KRPQ & Fenlo insurance companies.

Larkmoor Company is a general contractor specialized in the restoration industry for both residential and commercial properties.
We have incorporated the best technology tools and partnered with a network of industry professionals across the country to provide the most efficient and comprehensive service available.
Website under construction: www.thelarkmoorcompany.example

Target Market(s)

Insurance Sale Agents

Industry/Entity Type

Residential

Requirements
Must have
• Brightshield, Vantacover & KRPQ & Halvey Dresmit logos. Space to reproduce business card on back.. Looking for concept deign where we can work w/ local designer if necessary to finalize. Open to different sized flyer dependent on design.

```html
<!DOCTYPE html>
<html lang="en">
<head>
<meta charset="utf-8">
<title>Larkmoor Company – Claims Support Flyer</title>
<link href="https://fonts.googleapis.com/css2?family=PT+Sans:ital,wght@0,400;0,700;1,700&family=Cinzel:wght@600&display=swap" rel="stylesheet">
<style>
  :root {
    --ink: #111111;
    --orange: #f7a823;
    --gold: #e9a52a;
    --white: #ffffff;
    --photo-a: #1e3f8a;
    --photo-b: #9fb6d8;
    --photo-c: #e7eef7;
  }
  * { box-sizing: border-box; margin: 0; padding: 0; }
  html, body { width: 776px; height: 1200px; overflow: hidden; background: var(--white); }
  body { font-family: "PT Sans", Arial, sans-serif; color: var(--ink); }
  .flyer { position: relative; width: 776px; height: 1200px; overflow: hidden; background: var(--white); }

  .header { position: absolute; inset: 0 0 auto 0; height: 176px; }
  .header svg { position: absolute; inset: 0; }
  .brand {
    position: absolute; left: 36px; top: 52px; width: 300px;
    display: flex; align-items: center; gap: 14px;
    font-family: "Cinzel", Georgia, serif; font-weight: 600; font-size: 25px;
    color: var(--gold); letter-spacing: 0.5px;
  }
  .brand-square { width: 18px; height: 18px; background: var(--gold); flex: none; }
  .contact { position: absolute; right: 26px; top: 20px; text-align: right; }
  .contact-email { font-size: 23px; line-height: 1.2; }
  .contact-phone { font-size: 37px; line-height: 1.15; }

  .hero-photo {
    position: absolute; left: 0; top: 180px; width: 776px; height: 418px;
    background: linear-gradient(160deg, var(--photo-c) 0%, var(--photo-b) 35%, var(--photo-a) 100%);
  }

  .badge {
    position: absolute; left: 340px; top: 584px; width: 436px; height: 100px;
    background: var(--orange);
    clip-path: polygon(28px 0, 100% 0, 100% 100%, 0 100%);
    display: flex; flex-direction: column; justify-content: center; align-items: center;
    font-weight: 700; font-style: italic; font-size: 29px; line-height: 1.2;
    text-transform: uppercase; color: var(--ink); text-align: center;
  }

  .intro {
    position: absolute; left: 34px; top: 608px; width: 712px;
    font-size: 27.5px; line-height: 1.26;
  }
  .intro-spacer { float: right; width: 400px; height: 100px; }

  .about {
    position: absolute; left: 0; top: 864px; width: 776px; height: 236px;
    background: var(--ink); color: var(--white);
    padding: 16px 30px 0 34px; font-size: 22.5px; line-height: 1.3;
  }

  .footer { position: absolute; left: 0; top: 1116px; width: 776px; height: 84px; }
  .footer svg { position: absolute; inset: 0; }
  .footer-url {
    position: absolute; left: 30px; top: 18px;
    font-size: 36px; color: var(--ink);
  }
</style>
</head>
<body>
<main class="flyer">
  <header class="header">
    <svg width="776" height="176" viewBox="0 0 776 176" aria-hidden="true">
      <rect width="776" height="176" fill="var(--ink)"/>
      <polygon points="418,0 776,0 776,96 368,96" fill="var(--orange)"/>
      <polygon points="446,0 776,0 776,90 400,90" fill="var(--white)"/>
      <polygon points="640,96 776,96 776,176 592,176" fill="var(--orange)"/>
    </svg>
    <div class="brand"><span class="brand-square"></span>Larkmoor Company</div>
    <div class="contact">
      <p class="contact-email">info@larkmoorcompany.example</p>
      <p class="contact-phone">(855) 4-LkRoof</p>
    </div>
  </header>

  <div class="hero-photo" role="img" aria-label="Photo of construction tools on blueprints: hard hat, paint cans, brush, tape measure and folding ruler"></div>

  <p class="intro">
    <span class="intro-spacer"></span>
    Combining the best management tools, experience staff, and commitment to quality, we minimize the stress of the restoration process. Our efficient system simplifies the complex and gets you back on your feet fast.
  </p>

  <div class="badge"><span>Claims Support</span><span>After a Cat Event</span></div>

  <section class="about">
    <p>Larkmoor Company is a general contractor specialized in the restoration industry for both residential and commercial properties. We have incorporated the best technology tools and partnered with a network of industry professionals across the country to provide the most efficient and comprehensive service available.</p>
  </section>

  <footer class="footer">
    <svg width="776" height="84" viewBox="0 0 776 84" aria-hidden="true">
      <rect width="776" height="84" fill="var(--orange)"/>
      <polygon points="0,0 520,0 490,84 0,84" fill="var(--white)"/>
    </svg>
    <p class="footer-url">www.larkmoorcompany.example</p>
  </footer>
</main>
</body>
</html>
```